Brevolt custom business card design

After a business card incorporating the attached logo, I want the following

Brevolt
-Aluminium Windows & doors
-cladding
-roof access systems
-labour hire
-disabled access audits and alterations
-general carpentry

F 7, 21 wren gully road, Tallowford 3942
Ph: 5937 2418
Fax: 5937 2451
Mob: 0400 731 946
Marcus@brevoltworks.example

Target Market(s)

Construction industry

Industry/Entity Type

Business

Contact Information for Business Card

As per brief

Font styles to use
Serif
Script

```html
<!DOCTYPE html>
<html lang="en">
<head>
<meta charset="utf-8">
<title>Brevolt business card</title>
<link rel="stylesheet" href="https://fonts.googleapis.com/css2?family=Open+Sans:wght@400;600;700&family=Fira+Sans:wght@600&display=swap">
<style>
  :root {
    --bg: #e9e6e0;
    --gold-deep: #8f7f0c;
    --gold: #b8a31a;
    --gold-light: #f2ea8c;
    --accent-red: #c4161c;
    --paper: #f7f7f5;
    --paper-shade: #e6e6e4;
    --ink: #1c1c1c;
    --band-black: #1f1d1e;
    --ghost: #dcdcdc;
  }
  * { box-sizing: border-box; margin: 0; padding: 0; }
  html, body { width: 1200px; height: 913px; overflow: hidden; }
  body {
    background: var(--bg);
    font-family: "Open Sans", Arial, sans-serif;
    color: var(--ink);
    position: relative;
  }
  .card {
    position: absolute;
    left: 250px;
    width: 700px;
    height: 400px;
    background: linear-gradient(160deg, #ffffff, var(--paper) 55%, var(--paper-shade));
    box-shadow: 0 10px 24px rgba(0,0,0,.18);
    overflow: hidden;
  }
  .card--front { top: 38px; }
  .card--back  { top: 475px; }

  .gold-band {
    position: absolute; left: 0; top: 0; width: 100%;
    background:
      radial-gradient(ellipse 40% 120% at 62% 30%, rgba(255,252,210,.85), rgba(255,252,210,0) 70%),
      linear-gradient(100deg, var(--gold-deep), var(--gold) 35%, var(--gold-light) 60%, var(--gold) 80%, var(--gold-deep));
  }
  .card--front .gold-band { height: 150px; border-bottom: 4px solid var(--accent-red); }
  .card--back .gold-band { height: 170px; }

  .brand-name {
    position: absolute;
    font-family: "Open Sans", Arial, sans-serif;
    font-weight: 700;
    color: var(--ink);
    letter-spacing: 1px;
    line-height: 1;
  }
  .card--front .brand-name { left: 40px; top: 82px; font-size: 56px; }
  .card--back .brand-name { left: 40px; top: 106px; font-size: 50px; }

  .service-list {
    position: absolute; left: 64px; top: 174px;
    font-size: 17px; line-height: 23px;
    list-style: disc;
  }
  .black-band {
    position: absolute; left: 0; bottom: 16px; width: 100%; height: 66px;
    background: var(--band-black);
  }

  .ghost-name {
    position: absolute; right: 24px; top: 268px;
    font-size: 92px; font-weight: 700; line-height: 1;
    color: var(--ghost);
    letter-spacing: 2px;
  }
  .contact {
    position: absolute; left: 60px;
  }
  .contact-row {
    display: flex; align-items: center; gap: 10px;
    margin-bottom: 4px;
  }
  .contact-row svg { width: 16px; height: 16px; flex: none; }
  .contact--address { top: 190px; font-size: 15px; }
  .divider {
    position: absolute; left: 60px; top: 252px;
    width: 310px; height: 1.5px; background: var(--ink);
  }
  .contact--phones { top: 268px; font-family: "Fira Sans", Arial, sans-serif; font-weight: 600; font-size: 21px; }
  .contact--phones .contact-row { margin-bottom: 3px; }
</style>
</head>
<body>

<section class="card card--front" aria-label="Card front">
  <div class="gold-band"></div>
  <div class="brand-name">Brevolt</div>
  <ul class="service-list">
    <li>Aluminium Windows &amp; doors</li>
    <li>Cladding</li>
    <li>Roof access systems</li>
    <li>Labour hire</li>
    <li>Disabled access audits and alterations</li>
    <li>General carpentry</li>
  </ul>
  <div class="black-band"></div>
</section>

<section class="card card--back" aria-label="Card back">
  <div class="gold-band"></div>
  <div class="brand-name">Brevolt</div>
  <div class="ghost-name" aria-hidden="true">Brevolt</div>

  <div class="contact contact--address">
    <div class="contact-row">
      <svg viewBox="0 0 16 16"><circle cx="8" cy="8" r="7.2" fill="none" stroke="#1c1c1c" stroke-width="1.2"/><path d="M8 3.8a2.6 2.6 0 0 0-2.6 2.6C5.4 8.6 8 12 8 12s2.6-3.4 2.6-5.6A2.6 2.6 0 0 0 8 3.8z" fill="#1c1c1c"/><circle cx="8" cy="6.4" r="1" fill="#fff"/></svg>
      <span>F 7, 21 wren gully road, Tallowford 3942</span>
    </div>
    <div class="contact-row">
      <svg viewBox="0 0 16 16"><circle cx="8" cy="8" r="7.2" fill="none" stroke="#1c1c1c" stroke-width="1.2"/><rect x="4" y="5.2" width="8" height="5.6" fill="#1c1c1c"/><path d="M4 5.4l4 3 4-3" fill="none" stroke="#fff" stroke-width=".9"/></svg>
      <span>Marcus@brevoltworks.example</span>
    </div>
  </div>

  <div class="divider"></div>

  <div class="contact contact--phones">
    <div class="contact-row">
      <svg viewBox="0 0 16 16"><circle cx="8" cy="8" r="7.2" fill="none" stroke="#1c1c1c" stroke-width="1.2"/><path d="M5.2 4.2l1.6-.4 1 2.2-1 .8a5 5 0 0 0 2.4 2.4l.8-1 2.2 1-.4 1.6c-3.6.4-7-3-6.6-6.6z" fill="#1c1c1c"/></svg>
      <span>5937 2418</span>
    </div>
    <div class="contact-row">
      <svg viewBox="0 0 16 16"><circle cx="8" cy="8" r="7.2" fill="none" stroke="#1c1c1c" stroke-width="1.2"/><rect x="5.8" y="3.6" width="4.4" height="8.8" rx=".8" fill="#1c1c1c"/><rect x="6.5" y="4.6" width="3" height="5.6" fill="#fff"/></svg>
      <span>0400 731 946</span>
    </div>
    <div class="contact-row">
      <svg viewBox="0 0 16 16"><circle cx="8" cy="8" r="7.2" fill="none" stroke="#1c1c1c" stroke-width="1.2"/><rect x="4" y="7" width="8" height="4.6" rx=".6" fill="#1c1c1c"/><rect x="5.4" y="4" width="5.2" height="3.4" fill="#1c1c1c"/><rect x="5.4" y="9.6" width="5.2" height="1" fill="#fff"/></svg>
      <span>5937 2451</span>
    </div>
  </div>
</section>

</body>
</html>
```